Business Cards for IT Consulting Company (Managed Service Provider)

I am looking to have some business cards printed and would like some designs. We are an IT Consulting company based in Vancouver BC. I would like a nice clean and modern look to the cards. I have uploaded all the versions of my logo so parts can be used as needed. Here is a snippit from our website homepage:

Kelbrook Systems Ltd. is an IT Solutions Partner located in Vancouver BC, Canada. We offer IT solutions and support to customers in the greater Vancouver Area. With expertise in Microsoft platforms, as well as Linux and Mac OSX and over 12 years experience in the IT industry, Kelbrook Systems is dedicated to offering our clients top quality service and products. We take pride in the solutions we offer our customers. The greatest compliment a client can give us is to recommend our services.

Kelbrook Systems Ltd. offers a wide range of IT services from onsite service to remote support and managed service solutions. This allows clients to choose the support path that best suits their company’s needs. Supporting many different sized companies from small to enterprise level over the past 12 years Kelbrook Systems has the experience and expertise needed to ensure things run smoothly. Allowing our clients to focus on doing business.

Revolutionizing the way IT services are delivered.

Kelbrook Systems is dedicated to providing our clients with IT solutions that work and grow with them for years to come. This philosophy helps save money in the long run instead of replacing equipment constantly. Far too often IT solutions are not well thought out and while possibly solving the problem at hand, require replacement due to growth or quality within a very short time frame. Kelbrook Systems takes pride in providing solutions that will last and be able to accommodate growth without the need for replacement.

Industry/Entity Type

Information Technology

Contact Information for Business Card

Kelbrook Systems Ltd.
(Employee Name)
Eml: (Employees Email Address)
Web: kelbrook.me
Ph: 604-555-0142

Font styles to use
Serif
Sans Serif

Requirements
Must have
• The Company logo and company colors.
Nice to have
• - Our tag line: "Revolutionizing IT Services" or "Revolutionizing the way IT services are delivered."
• - Also I really like the idea of nature and technology together blending which is sort of where my logo came from so integrating that somehow onto the business cards would be great.

```html
<!DOCTYPE html>
<html lang="en">
<head>
<meta charset="utf-8">
<title>Kelbrook Systems Ltd. — Business Cards</title>
<link rel="stylesheet" href="https://fonts.googleapis.com/css2?family=Montserrat:wght@500;600;700&family=Roboto:ital,wght@0,400;1,400&display=swap">
<style>
  :root {
    --backdrop: #b3b1b2;
    --card-dark: #1f1f20;
    --card-light: #f1f1f1;
    --brand-blue: #1a8ad3;
    --brand-grey: #4a4a4a;
    --rule-dark: #3a3a3c;
    --text-light: #e4e4e4;
    --text-body: #454545;
    --text-muted: #555555;
  }
  * { margin: 0; padding: 0; box-sizing: border-box; }
  html, body {
    width: 1200px; height: 1200px; overflow: hidden;
    background: var(--backdrop);
  }
  .canvas { position: relative; width: 1200px; height: 1200px; }

  .card { position: absolute; width: 712px; height: 418px; }

  /* Front card */
  .card-front { left: 238px; top: 118px; background: var(--card-dark); }
  .card-front .wordmark {
    position: absolute; left: 0; right: 0; top: 176px;
    display: flex; justify-content: center; align-items: center; gap: 16px;
  }
  .wordmark-dot { width: 22px; height: 22px; border-radius: 50%; background: var(--brand-blue); flex: none; }
  .wordmark-name {
    font-family: "Montserrat", sans-serif; font-weight: 600;
    font-size: 44px; letter-spacing: 0.5px; color: var(--brand-blue); white-space: nowrap;
  }
  .tagline {
    position: absolute; left: 0; right: 0; top: 376px;
    display: flex; justify-content: center; align-items: center; gap: 16px;
  }
  .tagline-rule { width: 110px; height: 3px; background: var(--brand-blue); }
  .tagline-text {
    font-family: "Montserrat", sans-serif; font-weight: 500;
    font-size: 18px; color: var(--text-light); white-space: nowrap;
  }

  /* Back card */
  .card-back { left: 231px; top: 644px; background: var(--card-light); }
  .accent-band { position: absolute; left: 0; top: 0; bottom: 0; width: 59px; background: var(--brand-blue); }
  .accent-rule { position: absolute; left: 59px; top: 0; bottom: 0; width: 7px; background: var(--brand-grey); }
  .card-back .wordmark {
    position: absolute; left: 107px; top: 66px;
    display: flex; align-items: center; gap: 14px;
  }
  .card-back .wordmark-name { font-size: 38px; }
  .person { position: absolute; left: 106px; top: 202px; }
  .person-name {
    font-family: "Montserrat", sans-serif; font-weight: 700;
    font-size: 26px; color: var(--brand-blue); line-height: 1.2;
  }
  .person-role {
    font-family: "Roboto", sans-serif; font-style: italic;
    font-size: 16px; color: var(--text-muted); margin-top: 4px;
  }
  .contact-list { position: absolute; left: 106px; top: 294px; list-style: none; }
  .contact-item {
    display: flex; align-items: center; gap: 16px; height: 27.5px;
    font-family: "Roboto", sans-serif; font-size: 18px; color: var(--text-body);
  }
  .contact-icon { width: 18px; height: 18px; flex: none; }
</style>
</head>
<body>
<main class="canvas">

  <section class="card card-front" aria-label="Card front">
    <div class="wordmark">
      <span class="wordmark-dot"></span>
      <span class="wordmark-name">Kelbrook Systems Ltd.</span>
    </div>
    <div class="tagline">
      <span class="tagline-rule"></span>
      <span class="tagline-text">Revolutionizing IT Services</span>
      <span class="tagline-rule"></span>
    </div>
  </section>

  <section class="card card-back" aria-label="Card back">
    <div class="accent-band"></div>
    <div class="accent-rule"></div>

    <div class="wordmark">
      <span class="wordmark-dot"></span>
      <span class="wordmark-name">Kelbrook Systems Ltd.</span>
    </div>

    <div class="person">
      <p class="person-name">Daniel Hart</p>
      <p class="person-role">Managing Director</p>
    </div>

    <ul class="contact-list">
      <li class="contact-item">
        <svg class="contact-icon" viewBox="0 0 18 18" aria-hidden="true">
          <path d="M2 6c0-2 3-3 7-3s7 1 7 3v1.5h-3.5V6h-7v1.5H2z" fill="#1a8ad3"/>
          <path d="M5 8h8l2 7H3z" fill="#1a8ad3"/>
          <circle cx="9" cy="11.5" r="1.8" fill="#f1f1f1"/>
        </svg>
        <span>604-555-0142</span>
      </li>
      <li class="contact-item">
        <svg class="contact-icon" viewBox="0 0 18 18" aria-hidden="true">
          <circle cx="9" cy="9" r="7" fill="#1a8ad3"/>
          <g fill="none" stroke="#f1f1f1" stroke-width="1">
            <ellipse cx="9" cy="9" rx="3" ry="7"/>
            <line x1="2" y1="9" x2="16" y2="9"/>
            <line x1="3" y1="5.5" x2="15" y2="5.5"/>
            <line x1="3" y1="12.5" x2="15" y2="12.5"/>
          </g>
        </svg>
        <span>www.kelbrook.me</span>
      </li>
      <li class="contact-item">
        <svg class="contact-icon" viewBox="0 0 18 18" aria-hidden="true">
          <rect x="1.5" y="4" width="15" height="10.5" fill="#1a8ad3"/>
          <path d="M1.5 4l7.5 6 7.5-6" fill="none" stroke="#f1f1f1" stroke-width="1.2"/>
        </svg>
        <span>support@kelbrook.me</span>
      </li>
    </ul>
  </section>

</main>
</body>
</html>
```